Business Association needs street banner design promoting business district.

We are a business association that manages a commercial district of small family owned businesses. We would like to install banners (30 inches wide by 60 inches long) on street lights. The banners will include our logo and the name of the sponsor (we will need a space for the sponsor information). We will also need a space to include a photo of the sponsoring business (this space needs to be large). The banners are intended to promote the local small businesses. For more information on our organization, our web site is www.larkmoorba.org.

Target Market(s)

Member businesses and customers.

Industry/Entity Type

Small Business

Font styles to use
Sans Serif

Requirements
Must have
• Any images or type must be large enough for pedestrians to read from a distance. Brights colors. No copy 4 inches from top or bottom (the banners will be folded and sewn). These banners will be installed on street lights (see example image in files). Please design banner in Adobe Illustrator.
• Text on banner: "Welcome to Larkmoor!" Please include logo on banner.

```html
<!DOCTYPE html>
<html lang="en">
<head>
<meta charset="utf-8">
<title>Welcome to Larkmoor – Street Banner</title>
<link rel="stylesheet" href="https://fonts.googleapis.com/css2?family=Great+Vibes&family=Montserrat:wght@500;700;800&display=swap">
<style>
  :root {
    --navy: #1b2a6b;
    --deep-blue: #1a55b0;
    --sky: #19aee8;
    --pale: #e8f6fd;
    --white: #ffffff;
    --yellow: #f7e21b;
    --ink: #1c2550;
    --ring: #1f7fd0;
  }
  html, body {
    margin: 0;
    padding: 0;
    width: 1200px;
    height: 2400px;
    overflow: hidden;
    background: var(--white);
  }
  .banner {
    position: relative;
    width: 1200px;
    height: 2400px;
    overflow: hidden;
    background: linear-gradient(to bottom,
      var(--navy) 0%,
      var(--deep-blue) 16%,
      var(--sky) 38%,
      var(--sky) 52%,
      #8fd6f4 68%,
      var(--pale) 80%,
      var(--white) 92%);
    font-family: "Montserrat", Arial, sans-serif;
  }
  .stripes {
    position: absolute;
    inset: 0;
  }
  .headline {
    position: absolute;
    top: 250px;
    left: 0;
    width: 100%;
    text-align: center;
    color: var(--yellow);
  }
  .headline__welcome {
    display: block;
    font-family: "Great Vibes", cursive;
    font-size: 190px;
    line-height: 1;
  }
  .headline__to {
    display: block;
    font-weight: 700;
    font-size: 66px;
    line-height: 1;
    margin-top: 6px;
  }
  .headline__place {
    display: block;
    font-weight: 800;
    font-size: 150px;
    line-height: 1.05;
    letter-spacing: 2px;
  }
  .photo-slot {
    position: absolute;
    left: 600px;
    top: 1172px;
    width: 960px;
    height: 960px;
    margin: -480px 0 0 -480px;
    border-radius: 50%;
    background: var(--white);
    box-shadow: 0 0 0 18px #4fb8ec, 0 0 0 30px var(--ring);
    display: flex;
    align-items: center;
    justify-content: center;
  }
  .photo-slot__label {
    font-family: "Montserrat", Arial, sans-serif;
    font-weight: 500;
    font-size: 62px;
    color: #111111;
  }
  .association {
    position: absolute;
    top: 1850px;
    left: 0;
    width: 100%;
    text-align: center;
    color: var(--ink);
  }
  .association__dot {
    display: block;
    width: 150px;
    height: 150px;
    margin: 0 auto 30px;
    border-radius: 50%;
    background: var(--ink);
  }
  .association__name {
    display: block;
    font-weight: 800;
    font-size: 62px;
    line-height: 1.05;
  }
  .association__tagline {
    display: block;
    margin-top: 12px;
    font-weight: 500;
    font-size: 22px;
    letter-spacing: 1px;
    text-transform: uppercase;
  }
</style>
</head>
<body>
  <main class="banner">
    <svg class="stripes" width="1200" height="2400" viewBox="0 0 1200 2400" aria-hidden="true">
      <g stroke="#ffffff" stroke-opacity="0.35" stroke-width="4">
        <line x1="-300" y1="0" x2="500" y2="2400"/>
        <line x1="-180" y1="0" x2="620" y2="2400"/>
        <line x1="-60" y1="0" x2="740" y2="2400"/>
        <line x1="60" y1="0" x2="860" y2="2400"/>
        <line x1="180" y1="0" x2="980" y2="2400"/>
        <line x1="300" y1="0" x2="1100" y2="2400"/>
        <line x1="420" y1="0" x2="1220" y2="2400"/>
        <line x1="540" y1="0" x2="1340" y2="2400"/>
        <line x1="660" y1="0" x2="1460" y2="2400"/>
        <line x1="780" y1="0" x2="1580" y2="2400"/>
        <line x1="900" y1="0" x2="1700" y2="2400"/>
        <line x1="1020" y1="0" x2="1820" y2="2400"/>
        <line x1="1140" y1="0" x2="1940" y2="2400"/>
        <line x1="-420" y1="0" x2="380" y2="2400"/>
        <line x1="-540" y1="0" x2="260" y2="2400"/>
        <line x1="-660" y1="0" x2="140" y2="2400"/>
        <line x1="-780" y1="0" x2="20" y2="2400"/>
      </g>
    </svg>

    <h1 class="headline">
      <span class="headline__welcome">Welcome</span>
      <span class="headline__to">TO</span>
      <span class="headline__place">LARKMOOR!</span>
    </h1>

    <div class="photo-slot" role="img" aria-label="Photo of the sponsoring business">
      <span class="photo-slot__label">PHOTO</span>
    </div>

    <footer class="association">
      <span class="association__dot"></span>
      <span class="association__name">LARKMOOR<br>BUSINESS ASSOCIATION</span>
      <span class="association__tagline">Harbor Valley's International Marketplace</span>
    </footer>
  </main>
</body>
</html>
```